Corvane Holdings needs a business card

I would like the card to be simple but modern and elegant.
I like black and white.
or black and gold.
we are a private finance lender and also are involved in property and property developments.

please look at the business card photos i provided i would like C.H only one one side and all the other details on the other side use fonts that tie in with my theme.

Industry/Entity Type

Finance

Contact Information for Business Card

Corvane Holdings (C.H) Elliot Marbury M: 0413586102 E: elliotmar@examplemail.net

Font styles to use
Other font styles liked:
• Use fonts that would reflect our business

Colors
000000
ffffff

Requirements
Must have
• one side of details
• other side has either C.H or Corvane Holdings like in the photos provided

```html
<!DOCTYPE html>
<html lang="en">
<head>
<meta charset="utf-8">
<title>Corvane Holdings – Business Card</title>
<link rel="stylesheet" href="https://fonts.googleapis.com/css2?family=Ubuntu:wght@300;400;500;700&display=swap">
<style>
  :root {
    --card-black: #050505;
    --gold: #f6a41d;
    --backdrop: #e9e6e1;
    --card-shadow: rgba(0, 0, 0, 0.28);
  }

  * { box-sizing: border-box; margin: 0; padding: 0; }

  html, body {
    width: 1200px;
    height: 789px;
    overflow: hidden;
  }

  body {
    background: var(--backdrop);
    font-family: "Ubuntu", "Helvetica Neue", Arial, sans-serif;
    position: relative;
  }

  .card {
    position: absolute;
    top: 237px;
    width: 520px;
    height: 315px;
    background: var(--card-black);
    box-shadow: 0 10px 28px var(--card-shadow);
    color: var(--gold);
  }

  .card--monogram { left: 50px; }
  .card--details  { left: 630px; }

  /* Monogram side */
  .monogram {
    position: absolute;
    left: 0;
    right: 0;
    top: 78px;
    text-align: center;
    font-weight: 400;
    font-size: 64px;
    letter-spacing: 2px;
    line-height: 1;
  }

  /* Details side */
  .wordmark {
    position: absolute;
    left: 60px;
    top: 178px;
    font-weight: 700;
    line-height: 0.95;
  }

  .wordmark__primary {
    display: block;
    font-size: 42px;
    letter-spacing: -0.5px;
  }

  .wordmark__secondary {
    display: block;
    font-size: 25px;
    margin-left: 62px;
    letter-spacing: 1px;
  }

  .contact {
    position: absolute;
    left: 305px;
    top: 70px;
    width: 185px;
    text-align: center;
  }

  .contact__name {
    font-weight: 500;
    font-size: 18px;
    padding-bottom: 8px;
    border-bottom: 1px solid var(--gold);
  }

  .contact__phone {
    font-weight: 400;
    font-size: 12px;
    padding: 9px 0 8px;
    border-bottom: 1px solid var(--gold);
    letter-spacing: 0.3px;
  }

  .contact__email {
    font-weight: 400;
    font-size: 12px;
    padding-top: 10px;
    letter-spacing: 0.2px;
  }
</style>
</head>
<body>

  <section class="card card--monogram" aria-label="Card front">
    <p class="monogram">C.H</p>
  </section>

  <section class="card card--details" aria-label="Card back">
    <p class="wordmark">
      <span class="wordmark__primary">Corvane</span>
      <span class="wordmark__secondary">Holdings</span>
    </p>

    <div class="contact">
      <p class="contact__name">Elliot Marbury</p>
      <p class="contact__phone">0413-586-102</p>
      <p class="contact__email">elliotmar@examplemail.net</p>
    </div>
  </section>

</body>
</html>
```